Corliss Homes Website for luxury custom home builder with endless detail

Modern website for luxury custom home builder. Simple and easy for viewers to understand what we do. New company formed by retired custom home builder. Company concept is to simplify the building experience with modern technology and introduce a simple pricing strategy for the client. Website must flow. Prefer page less design or possibly something that is up and coming within the web design community. Two galleries: INTERIOR and EXTERIOR. I would like two click on box's when the website is opened showing the galleries as a centerpiece and would also prefer them to play as a slide show. The page needs to fit the entire screen in size. We would like to use Grey, Black and White or the shade of blue that is in our company logo. I would like to see one of my uploaded photos to be in the background. I would also like a 3rd box that will play some type of animated video describing what we do and what our process is. Hoping this would be more interactive for the viewer than clicking on buttons and navigating around wasting time.

Target Market(s)

affluent buyers ages 30-60 who want to built anything from large estates to downsized luzury homes for the retired crowd.

Industry/Entity Type

Home Builder

Number of Pages Required

1 page

Font styles to use
Sans Serif

Colors
33a6d7
000000
333333
5c5c5c
9d9d9d
d9d9d9

Requirements
Must have
• Logo and name at top of page. I would like a pageless web design that includes two gallery box's (Interior and Exterior photos) side by side on the first page. I would also like a 3rd box that will be a eVideo explaining what we do and how we do it. I want as little text as possible. I would like the background to be of one of my interior photos that will flow best and pop when the page loads.

```html
<!DOCTYPE html>
<html lang="en">
<head>
<meta charset="utf-8">
<title>Corliss Homes</title>
<link href="https://fonts.googleapis.com/css2?family=Open+Sans:wght@300;400;600&family=Roboto:wght@300;400;500&display=swap" rel="stylesheet">
<style>
:root{
  --blue:#33a6d7;
  --black:#000000;
  --ink:#333333;
  --mid:#5c5c5c;
  --soft:#9d9d9d;
  --line:#d9d9d9;
  --page:#f1f1f1;
  --white:#ffffff;
  --footer:#2b2b2b;
}
*{box-sizing:border-box;margin:0;padding:0}
html,body{width:711px;height:1200px;overflow:hidden}
body{background:var(--page);font-family:"Open Sans",Arial,sans-serif;color:var(--ink);position:relative}

.site-header{position:absolute;top:0;left:0;width:711px;height:66px;background:var(--white);z-index:3}
.brand{position:absolute;left:42px;top:10px;width:120px;text-align:center}
.brand-square{display:block;width:28px;height:28px;margin:0 auto 4px;background:var(--blue)}
.brand-name{font-family:"Roboto",sans-serif;font-size:13px;font-weight:500;color:var(--blue)}
.main-nav{position:absolute;right:26px;top:0;display:flex;height:66px}
.main-nav a{display:flex;align-items:center;justify-content:center;width:58px;font-family:"Roboto",sans-serif;font-size:9.5px;color:var(--mid);text-decoration:none}
.main-nav a.active{background:var(--blue);color:var(--white)}

.hero{position:absolute;top:66px;left:0;width:711px;height:408px;background:linear-gradient(180deg,#8fb8d8 0%,#a9b7a6 30%,#a8725a 52%,#3f8fc0 66%,#8a7d6c 82%,#cbb7a3 100%)}
.hero-title{position:absolute;top:128px;left:0;width:100%;text-align:center;color:var(--white);font-family:"Roboto",sans-serif}
.hero-title h1{font-size:32px;font-weight:400;letter-spacing:.5px}
.hero-title p{font-size:20px;font-weight:300;margin-top:6px}

.welcome{position:absolute;left:66px;top:315px;width:584px;height:147px;background:var(--white);box-shadow:0 3px 8px rgba(0,0,0,.15);text-align:center;padding:18px 48px 0;z-index:2}
.welcome h2{font-family:"Roboto",sans-serif;font-size:21px;font-weight:300;color:var(--ink)}
.welcome h2 span{color:var(--blue)}
.welcome p{font-size:7px;line-height:11px;color:var(--soft);margin-top:10px}
.read-more{display:inline-block;margin-top:10px;font-size:11px;font-weight:600;color:var(--ink)}

.section-title{position:absolute;left:0;width:711px;text-align:center;font-family:"Roboto",sans-serif;font-size:15px;font-weight:400;color:var(--blue);letter-spacing:.5px}
.section-note{position:absolute;left:150px;width:411px;text-align:center;font-size:6.5px;line-height:10px;color:var(--soft)}

.gallery-tabs{position:absolute;top:566px;left:0;width:711px;display:flex;justify-content:center;gap:12px}
.gallery-tabs span{width:112px;height:25px;border-radius:4px;display:flex;align-items:center;justify-content:center;color:var(--white);font-family:"Roboto",sans-serif;font-size:11px}
.tab-interior{background:var(--blue)}
.tab-exterior{background:var(--mid)}

.gallery-row{position:absolute;top:621px;left:59px;width:590px;height:119px;display:flex;justify-content:space-between}
.gallery-row div{width:136px;height:119px;border:3px solid var(--white);box-shadow:0 1px 3px rgba(0,0,0,.2)}
.ph-1{background:linear-gradient(180deg,#8db5d6,#b27a55 55%,#8a6a45)}
.ph-2{background:linear-gradient(160deg,#3a2a20,#8c5a33 55%,#c49a6b)}
.ph-3{background:linear-gradient(180deg,#7fb0d8,#a58263 50%,#5e8b3e)}
.ph-4{background:linear-gradient(180deg,#6f9a5a,#5a8abf 55%,#3f7a3a)}
.arrow{position:absolute;color:var(--soft);font-size:14px}

.video-frame{position:absolute;left:76px;top:884px;width:559px;height:223px;border:4px solid var(--white);box-shadow:0 2px 6px rgba(0,0,0,.2);background:linear-gradient(160deg,#5a2e1a,#9a6436 40%,#c7a07a 60%,#6b3a1f)}
.play{position:absolute;left:253px;top:86px}

.site-footer{position:absolute;left:0;top:1154px;width:711px;height:46px;background:var(--footer);color:var(--soft);font-size:8px}
.copyright{position:absolute;left:22px;top:18px}
.social{position:absolute;right:42px;top:15px;display:flex;gap:5px}
.social span{width:15px;height:15px}
.lang{position:absolute;right:14px;top:18px;color:var(--white)}
</style>
</head>
<body>
<header class="site-header">
  <div class="brand"><span class="brand-square"></span><span class="brand-name">Corliss Homes</span></div>
  <nav class="main-nav">
    <a class="active">Home</a><a>About Us</a><a>Service</a><a>Blogs</a><a>News</a><a>Contact Us</a>
  </nav>
</header>

<section class="hero" role="img" aria-label="Courtyard of a Spanish-style luxury home with a swimming pool and lounge chairs">
  <div class="hero-title"><h1>Corliss Homes</h1><p>We are luxury custom home builder</p></div>
</section>

<section class="welcome">
  <h2>WELCOME TO <span>Corliss Homes</span></h2>
  <p>We design and build custom luxury homes from the first sketch to the final walkthrough. Our team pairs decades of craftsmanship with modern planning tools, so every client sees clear pricing, steady progress and a home shaped around the way they live, from grand estates to refined smaller residences.</p>
  <span class="read-more">Read More &gt;&gt;</span>
</section>

<h2 class="section-title" style="top:498px">GALLERIES</h2>
<p class="section-note" style="top:524px">Browse finished interiors and exteriors from recent projects. Each home reflects careful detail, lasting materials and a plan built around its owners.</p>
<div class="gallery-tabs"><span class="tab-interior">INTERIOR</span><span class="tab-exterior">EXTERIOR</span></div>
<div class="gallery-row">
  <div class="ph-1" role="img" aria-label="Stucco home exterior with arched entry"></div>
  <div class="ph-2" role="img" aria-label="Wood-paneled interior with staircase"></div>
  <div class="ph-3" role="img" aria-label="Home exterior with lawn and arches"></div>
  <div class="ph-4" role="img" aria-label="Backyard with fire pit and pool"></div>
</div>

<h2 class="section-title" style="top:811px">OUR VIDEOS</h2>
<p class="section-note" style="top:838px">Watch how a Corliss home comes together, from first meeting and simple pricing to design, construction and the day you receive your keys.</p>
<span class="arrow" style="left:48px;top:985px">&#8249;</span>
<span class="arrow" style="left:654px;top:985px">&#8250;</span>
<div class="video-frame" role="img" aria-label="Video still of a luxury kitchen with wood cabinets and a stone island">
  <svg class="play" width="52" height="52" viewBox="0 0 52 52"><circle cx="26" cy="26" r="25" fill="rgba(255,255,255,.55)"/><path d="M21 16 L37 26 L21 36 Z" fill="#ffffff"/></svg>
</div>

<footer class="site-footer">
  <span class="copyright">Copyright@Corliss Homes 2014</span>
  <div class="social">
    <span style="background:#3b5998"></span><span style="background:#33a6d7"></span><span style="background:#dd4b39"></span><span style="background:#5c5c5c"></span><span style="background:#33a6d7"></span>
  </div>
  <span class="lang">EN</span>
</footer>
</body>
</html>
```